Small rum distillery looking for bottle design

Small rum distillery in Estonia. Looking for bottle lable design. It should be simple but at the same time point out from the variety of other bottles.
As we are a small nordic country, design can be some how nordic or represent our country. It can also have some connection with sailing or sea as we know it pirates love it.
Bottle we are using is Corvane 540

Industry/Entity Type

food and beverage

Other font styles liked:
• Baskerville

```html
<!DOCTYPE html>
<html lang="en">
<head>
<meta charset="utf-8">
<title>Haldre Distillery – Rum Label</title>
<link rel="stylesheet" href="https://fonts.googleapis.com/css2?family=Libre+Baskerville&family=Dancing+Script:wght@500&family=Roboto:wght@400&display=swap">
<style>
  :root {
    --backdrop: #c6e1c9;
    --label-white: #f7f7f7;
    --ink: #333333;
    --band: #3b3b3b;
    --band-text: #f0f0f0;
    --accent-red: #c8262b;
    --sail-blue: #2770b8;
    --sail-dark: #2f2f2f;
  }
  * { margin: 0; padding: 0; box-sizing: border-box; }
  html, body {
    width: 1200px;
    height: 835px;
    overflow: hidden;
    background: var(--backdrop);
  }
  .canvas {
    position: relative;
    width: 1200px;
    height: 835px;
  }

  /* Neck strip */
  .neck-strip {
    position: absolute;
    left: 190px;
    top: 150px;
    width: 70px;
    height: 500px;
    background: var(--label-white);
    display: flex;
    flex-direction: column;
    align-items: center;
    justify-content: space-between;
    padding: 40px 0 36px;
  }
  .neck-strip__name {
    writing-mode: vertical-rl;
    transform: rotate(180deg);
    font-family: "Libre Baskerville", serif;
    font-size: 30px;
    letter-spacing: 0.08em;
    color: var(--ink);
  }
  .neck-strip__mark {
    width: 34px;
    height: 34px;
    background: var(--accent-red);
  }

  /* Main label */
  .label {
    position: absolute;
    left: 330px;
    top: 118px;
    width: 680px;
    height: 600px;
  }
  .label__shape {
    position: absolute;
    inset: 0;
  }
  .label__content {
    position: absolute;
    inset: 0;
    display: flex;
    flex-direction: column;
    align-items: center;
  }
  .brand-mark {
    margin-top: 40px;
    width: 46px;
    height: 46px;
    background: var(--accent-red);
  }
  .brand-name {
    margin-top: 26px;
    font-family: "Libre Baskerville", serif;
    font-size: 58px;
    line-height: 1;
    letter-spacing: 0.04em;
    color: var(--ink);
    text-transform: uppercase;
  }
  .brand-rule {
    margin-top: 14px;
    width: 350px;
    height: 2px;
    background: var(--ink);
  }
  .brand-sub {
    margin-top: 12px;
    font-family: "Libre Baskerville", serif;
    font-size: 22px;
    letter-spacing: 0.3em;
    color: var(--ink);
    text-transform: uppercase;
  }
  .sail-artwork {
    margin-top: 16px;
    width: 150px;
    height: 170px;
    background: linear-gradient(160deg, var(--sail-blue) 0%, var(--sail-blue) 35%, #ffffff 50%, var(--sail-dark) 65%, var(--sail-dark) 100%);
  }
  .product-line {
    margin-top: 14px;
    font-family: "Dancing Script", cursive;
    font-weight: 500;
    font-size: 30px;
    color: var(--accent-red);
  }
  .spec-band {
    position: absolute;
    left: 0;
    right: 0;
    bottom: 0;
    height: 100px;
    display: flex;
    align-items: center;
    justify-content: center;
    font-family: "Roboto", sans-serif;
    font-size: 20px;
    color: var(--band-text);
    letter-spacing: 0.02em;
  }
  .spec-band__divider { margin: 0 16px; }
</style>
</head>
<body>
<div class="canvas">

  <aside class="neck-strip">
    <span class="neck-strip__name">HALDRE</span>
    <span class="neck-strip__mark"></span>
  </aside>

  <section class="label">
    <svg class="label__shape" width="680" height="600" viewBox="0 0 680 600" aria-hidden="true">
      <defs>
        <pattern id="teeth" width="10" height="6" patternUnits="userSpaceOnUse">
          <polygon points="0,6 5,0 10,6" fill="var(--band)"/>
        </pattern>
      </defs>
      <path d="M0,80 Q40,48 85,62 Q340,-25 595,62 Q640,48 680,80 V600 H0 Z" fill="var(--label-white)"/>
      <rect x="0" y="494" width="680" height="6" fill="url(#teeth)"/>
      <rect x="0" y="500" width="680" height="100" fill="var(--band)"/>
    </svg>

    <div class="label__content">
      <span class="brand-mark"></span>
      <h1 class="brand-name">Haldre</h1>
      <div class="brand-rule"></div>
      <p class="brand-sub">Haldre Distillery</p>
      <div class="sail-artwork" role="img" aria-label="Sail illustration in blue, white and black stripes"></div>
      <p class="product-line">Estonian Distillery Rum</p>
    </div>

    <div class="spec-band">
      <span>500 ml</span><span class="spec-band__divider">|</span><span>37.5% vol. alc.</span>
    </div>
  </section>

</div>
</body>
</html>
```